Brackwell + Osgood Architecture Ltd Stationary rebrand Lead designer to create a fresh clean modern...

We have recieved a great new logo design and now we are after a consistant fresh and modern stationary to match the new design. Business card design, Letter Head design, presentatnion folders and other stationery within the package. I have also added some of our existing layouts for presentation we would like updating with the new look, We would like a clean modern fresh design that looks visually pleasing on the page. we cant wait to see what you come up with!!!!

Target Market(s)

young professionals and middle age clients

Industry/Entity Type

Architect

Contact Information for Business Card

i have uploarded our orginal business card that has all the details attached.

Font styles to use
Sans Serif

Colors
000000
ffffff
d3d3d3

Requirements
Must have
• Logo and our contact information
Nice to have
• white sape around the card to give a clean look.

```html
<!DOCTYPE html>
<html lang="en">
<head>
<meta charset="utf-8">
<title>Brackwell + Osgood Architecture – Stationery</title>
<link rel="stylesheet" href="https://fonts.googleapis.com/css2?family=Quicksand:wght@400;500;700&display=swap">
<style>
:root{
  --black:#000000;
  --white:#ffffff;
  --grey:#d3d3d3;
  --ink:#1a1a1a;
  --rule:#777777;
  --faint:#f6f6f6;
  --shadow:rgba(0,0,0,.18);
}
*{box-sizing:border-box;margin:0;padding:0}
html,body{width:1200px;height:1200px;overflow:hidden;background:var(--white)}
body{position:relative;font-family:"Quicksand",sans-serif;color:var(--ink)}
.sheet{position:absolute;overflow:hidden;box-shadow:0 4px 10px var(--shadow)}
.card{left:71px;width:325px;height:194px}
.card--light{background:var(--white);border:1px solid #e4e4e4}
.card--dark{background:var(--black);color:var(--grey)}
.icon{width:7px;height:7px;fill:currentColor;flex:none}

/* brand lockup */
.brand{position:absolute;display:flex;flex-direction:column;align-items:center;text-align:center}
.brand__mark{background:currentColor;display:block}
.brand__name{font-weight:700;white-space:nowrap}
.brand__sub{font-weight:700;white-space:nowrap}

/* card 1 */
.c1{top:174px}
.c1 .brand{left:12px;top:12px;align-items:flex-start;color:var(--black)}
.c1 .brand__mark{width:34px;height:34px;margin-bottom:6px}
.c1 .brand__name{font-size:9px;letter-spacing:1px}
.c1 .brand__sub{font-size:5.5px;letter-spacing:3.4px;margin-top:2px}
.c1 .person{position:absolute;right:12px;top:104px;text-align:right}
.person__name{font-weight:700;font-size:13.5px;letter-spacing:.3px;color:var(--black)}
.person__role{font-size:7.5px;letter-spacing:1.2px}
.c1 .rule{position:absolute;left:12px;right:12px;top:128px;height:1px;background:var(--rule)}
.c1 .person__role{position:absolute;right:12px;top:129px}
.contacts{list-style:none;font-size:8.5px;line-height:11.6px}
.contacts li{display:flex;align-items:center;gap:6px}
.c1 .contacts{position:absolute;left:12px;top:142px}
.c1 .address{position:absolute;right:12px;top:142px;text-align:right;font-size:8.5px;line-height:11.6px;list-style:none}
.c1 .band{position:absolute;left:0;right:0;bottom:0;height:4px;background:var(--black)}

/* dark cards */
.c2{top:413px}.c4{top:879px}
.card--dark .brand{left:0;right:0;top:42px}
.card--dark .brand__mark{width:40px;height:40px;background:var(--grey);margin-bottom:10px}
.card--dark .brand__name{font-size:12px;letter-spacing:1.8px;color:var(--grey)}
.card--dark .brand__sub{font-size:6.5px;letter-spacing:6.2px;margin-top:3px;color:var(--grey)}
.card--dark .web{position:absolute;left:0;right:0;bottom:18px;text-align:center;font-size:9px;font-weight:700;letter-spacing:1px;color:var(--grey)}
.c2 .edge{position:absolute;left:0;right:0;bottom:0;height:3px;background:var(--grey)}

/* card 3 */
.c3{top:646px}
.c3 .brand{left:0;right:0;top:20px;color:var(--black)}
.c3 .brand__mark{width:30px;height:30px;margin-bottom:6px}
.c3 .brand__name{font-size:10px;letter-spacing:1.4px}
.c3 .brand__sub{font-size:5.5px;letter-spacing:5px;margin-top:2px}
.c3 .person{position:absolute;right:178px;top:114px;text-align:right}
.c3 .person__name{font-size:13px}
.c3 .divider{position:absolute;left:162px;top:107px;width:1px;height:40px;background:var(--black)}
.c3 .contacts{position:absolute;left:172px;top:106px;font-size:7.2px;line-height:10.8px}
.c3 .band{position:absolute;left:0;right:0;top:162px;height:11px;background:var(--black);color:var(--white);font-size:7.4px;line-height:11px;text-align:center}

/* letterhead */
.letterhead{left:446px;top:174px;width:688px;height:890px;background:var(--white);border:1px solid #e8e8e8}
.letterhead .brand{left:0;right:0;top:38px;color:var(--black)}
.letterhead .brand__mark{width:54px;height:54px;margin-bottom:14px}
.letterhead .brand__name{font-size:17px;letter-spacing:2.6px}
.letterhead .brand__sub{font-size:8.5px;letter-spacing:9.6px;margin-top:4px}
.watermark{position:absolute;left:0;right:0;top:560px;text-align:center;font-weight:700;font-size:52px;letter-spacing:2px;color:var(--faint);line-height:1.1}
.letterhead .contacts{position:absolute;left:36px;right:36px;top:826px;display:flex;justify-content:space-between;font-size:10.5px}
.letterhead .contacts li{gap:9px}
.letterhead .contacts .icon{width:9px;height:9px}
.letterhead .band{position:absolute;left:0;right:0;top:847px;height:24px;background:var(--black);color:var(--white);font-size:12.5px;line-height:24px;text-align:center;letter-spacing:.3px}
</style>
</head>
<body>
<svg width="0" height="0" style="position:absolute" aria-hidden="true">
  <symbol id="i-phone" viewBox="0 0 10 10"><path d="M2 0.5l1.8 2-1 1.2a6 6 0 0 0 3.5 3.5l1.2-1 2 1.8-1.3 1.5C4.5 9.5 0.5 5.5 0.5 1.8z"/></symbol>
  <symbol id="i-mobile" viewBox="0 0 10 10"><path d="M2.5 0h5v10h-5zM3.6 1.2v6.6h2.8V1.2z"/></symbol>
  <symbol id="i-mail" viewBox="0 0 10 10"><path d="M0 1.5h10v7H0zM1.2 2.6L5 5.3 8.8 2.6z"/></symbol>
  <symbol id="i-web" viewBox="0 0 10 10"><circle cx="5" cy="5" r="5"/></symbol>
</svg>

<!-- business card: white, detailed -->
<section class="sheet card card--light c1">
  <div class="brand">
    <span class="brand__mark"></span>
    <span class="brand__name">BRACKWELL + OSGOOD</span>
    <span class="brand__sub">ARCHITECTURE</span>
  </div>
  <div class="person"><p class="person__name">DANIEL BRACKWELL</p></div>
  <div class="rule"></div>
  <p class="person__role">Director</p>
  <ul class="contacts">
    <li><svg class="icon"><use href="#i-phone"/></svg>000 000 0000</li>
    <li><svg class="icon"><use href="#i-mobile"/></svg>sam_k@northfield.ch</li>
    <li><svg class="icon"><use href="#i-mail"/></svg>sam_k@northfield.ch</li>
    <li><svg class="icon"><use href="#i-web"/></svg>www.northfield.ch</li>
  </ul>
  <ul class="address">
    <li>48 Harlow Street</li>
    <li>Tenterton 7700</li>
    <li>PO Box 5184</li>
    <li>Tenterton 7740</li>
  </ul>
  <div class="band"></div>
</section>

<!-- business card: black back -->
<section class="sheet card card--dark c2">
  <div class="brand">
    <span class="brand__mark"></span>
    <span class="brand__name">BRACKWELL + OSGOOD</span>
    <span class="brand__sub">ARCHITECTURE</span>
  </div>
  <p class="web">www.northfield.ch</p>
  <div class="edge"></div>
</section>

<!-- business card: white, centred -->
<section class="sheet card card--light c3">
  <div class="brand">
    <span class="brand__mark"></span>
    <span class="brand__name">BRACKWELL + OSGOOD</span>
    <span class="brand__sub">ARCHITECTURE</span>
  </div>
  <div class="person">
    <p class="person__name">DANIEL BRACKWELL</p>
    <p class="person__role">Director</p>
  </div>
  <div class="divider"></div>
  <ul class="contacts">
    <li><svg class="icon"><use href="#i-phone"/></svg>03 412 5580</li>
    <li><svg class="icon"><use href="#i-mobile"/></svg>0275 861 302</li>
    <li><svg class="icon"><use href="#i-mail"/></svg>daniel@boarchitecture.co.nz</li>
    <li><svg class="icon"><use href="#i-web"/></svg>www.boarchitecture.co.nz</li>
  </ul>
  <p class="band">48 Harlow Street, Tenterton 7700 &nbsp;|&nbsp; PO Box 5184, Tenterton 7740</p>
</section>

<!-- business card: black back, alternate -->
<section class="sheet card card--dark c4">
  <div class="brand">
    <span class="brand__mark"></span>
    <span class="brand__name">BRACKWELL + OSGOOD</span>
    <span class="brand__sub">ARCHITECTURE</span>
  </div>
  <p class="web">www.northfield.ch</p>
</section>

<!-- letterhead -->
<section class="sheet letterhead">
  <div class="brand">
    <span class="brand__mark"></span>
    <span class="brand__name">BRACKWELL + OSGOOD</span>
    <span class="brand__sub">ARCHITECTURE</span>
  </div>
  <p class="watermark" aria-hidden="true">BRACKWELL<br>+ OSGOOD</p>
  <ul class="contacts">
    <li><svg class="icon"><use href="#i-phone"/></svg>03 412 5580</li>
    <li><svg class="icon"><use href="#i-mobile"/></svg>0275 861 302</li>
    <li><svg class="icon"><use href="#i-mail"/></svg>daniel@boarchitecture.co.nz</li>
    <li><svg class="icon"><use href="#i-web"/></svg>www.boarchitecture.co.nz</li>
  </ul>
  <p class="band">48 Harlow Street, Tenterton 7700 &nbsp;|&nbsp; PO Box 5184, Tenterton 7740</p>
</section>
</body>
</html>
```